Business Card Design Project

Corvexa logo will be provided after
Front

Bram Oskarsen- Construction Manager

Ph: (61) 07 53182907
boskarsen@corvexa.com.au
PO Box 83 Kelbarra 4529

Back
Corvexa
EPCM

Oil - Gas - Mining

Industry/Entity Type

Business

Font styles to use
Sans Serif

Colors
faa54b

Requirements
Must have
• White Back Ground

```html
<!DOCTYPE html>
<html lang="en">
<head>
<meta charset="utf-8">
<title>Corvexa Business Cards</title>
<link rel="stylesheet" href="https://fonts.googleapis.com/css2?family=Arimo:wght@400;700&display=swap">
<style>
  :root {
    --orange: #faa54b;
    --orange-deep: #f0922e;
    --ink: #111111;
    --paper: #ffffff;
    --backdrop: #ece9e6;
  }
  * { box-sizing: border-box; margin: 0; padding: 0; }
  html, body { width: 1200px; height: 960px; overflow: hidden; }
  body {
    background: var(--backdrop);
    font-family: "Arimo", Arial, sans-serif;
    color: var(--ink);
    position: relative;
  }
  .card {
    position: absolute;
    left: 240px;
    width: 720px;
    height: 420px;
    background: var(--paper);
    box-shadow: 0 6px 18px rgba(0,0,0,0.18);
    overflow: hidden;
  }
  .card--back { top: 40px; }
  .card--front { top: 500px; }

  .wordmark {
    position: absolute;
    font-weight: 700;
    letter-spacing: 4px;
    color: var(--ink);
    line-height: 1;
  }

  /* Back */
  .card--back .wordmark { left: 150px; top: 120px; font-size: 76px; }
  .tagline {
    position: absolute;
    left: 430px; top: 210px;
    font-size: 26px;
    letter-spacing: 1px;
  }
  .sector-band {
    position: absolute;
    left: 0; right: 0; bottom: 0;
    height: 84px;
    background: linear-gradient(90deg, var(--orange-deep), var(--orange));
    display: flex;
    justify-content: space-around;
    align-items: center;
    padding: 0 60px;
  }
  .sector {
    display: flex;
    align-items: center;
    gap: 12px;
    color: var(--paper);
    font-size: 20px;
  }
  .sector__dot {
    width: 20px; height: 20px;
    border-radius: 50%;
    background: var(--ink);
    display: flex; align-items: center; justify-content: center;
  }
  .sector__dot::after {
    content: "";
    width: 7px; height: 7px;
    border-radius: 50%;
    background: var(--orange);
  }

  /* Front */
  .card--front .wordmark { left: 70px; top: 150px; font-size: 78px; }
  .edge-lines--left {
    position: absolute;
    left: 14px; top: 0;
    width: 14px; height: 240px;
    border-left: 4px solid var(--orange);
    border-right: 4px solid var(--orange);
  }
  .edge-lines--bottom {
    position: absolute;
    left: 90px; right: 0; bottom: 10px;
    height: 14px;
    border-top: 4px solid var(--orange);
    border-bottom: 4px solid var(--orange);
  }
  .person {
    position: absolute;
    right: 40px; top: 40px;
    width: 230px;
  }
  .person__name {
    font-size: 26px;
    padding-bottom: 10px;
    border-bottom: 2px solid var(--ink);
  }
  .person__role {
    font-size: 17px;
    padding-top: 10px;
    text-align: right;
  }
  .contact {
    position: absolute;
    left: 90px; top: 270px;
    list-style: none;
    font-size: 19px;
  }
  .contact__item {
    display: flex;
    align-items: center;
    gap: 14px;
    height: 32px;
  }
  .contact__icon { width: 20px; height: 20px; flex: none; }
</style>
</head>
<body>

<section class="card card--back" aria-label="Card back">
  <div class="wordmark">CORVEXA</div>
  <div class="tagline">EPCM</div>
  <div class="sector-band">
    <span class="sector"><span class="sector__dot"></span>Oil</span>
    <span class="sector"><span class="sector__dot"></span>Gas</span>
    <span class="sector"><span class="sector__dot"></span>Mining</span>
  </div>
</section>

<section class="card card--front" aria-label="Card front">
  <div class="edge-lines--left"></div>
  <div class="edge-lines--bottom"></div>

  <div class="person">
    <p class="person__name">Bram Oskarsen</p>
    <p class="person__role">Construction Manager</p>
  </div>

  <div class="wordmark">CORVEXA</div>

  <ul class="contact">
    <li class="contact__item">
      <svg class="contact__icon" viewBox="0 0 20 20" aria-hidden="true">
        <path d="M2 7c0-3 3-4 8-4s8 1 8 4l-3 1-1-2H6L5 8z" fill="#111"/>
        <rect x="4" y="9" width="12" height="8" rx="1.5" fill="#111"/>
        <circle cx="10" cy="13" r="2" fill="#fff"/>
      </svg>
      (61) 07 53182907
    </li>
    <li class="contact__item">
      <svg class="contact__icon" viewBox="0 0 20 20" aria-hidden="true">
        <rect x="1" y="4" width="18" height="12" fill="#111"/>
        <path d="M1 4l9 7 9-7" fill="none" stroke="#fff" stroke-width="1.5"/>
      </svg>
      boskarsen@corvexa.com.au
    </li>
    <li class="contact__item">
      <svg class="contact__icon" viewBox="0 0 20 20" aria-hidden="true">
        <path d="M10 19C6 13 4 10 4 7.5a6 6 0 0 1 12 0C16 10 14 13 10 19z" fill="#111"/>
        <circle cx="10" cy="7.5" r="2.2" fill="#fff"/>
      </svg>
      PO Box 83 Kelbarra 4529
    </li>
  </ul>
</section>

</body>
</html>
```